Need a business card design. I am a Self Empowerment Life Coach.

A Life Coach is - a professional relationship designed to enhance an individual's ability to focus, make effective changes, develop oneself, achieve desired goals and maximize success in life. Coaching is about getting the very best out of someone and enabling them to make decisions that will improve their life. It is a unique way to help people look at where they are now and where they would like to be, and helps bridge the gap.

Bright Path Coaching is motivational, inspiring, positive, exciting and action driven. By raising awareness and encouraging others to take responsibility for their life, coaching can help people rise to their challenge and go further than you ever thought possible.

Industry/Entity Type

Business

Other font styles liked:
• Bookman Old Style

Requirements
Must have
• Marla Thorncastle, QTV-AR
• Self Empowerment Coach
• 318.557.6021
• mt@thebloomingpathcoach.example
• The attached logo
Nice to have
• I would like to see some designs portrait and some landscape

```html
<!DOCTYPE html>
<html lang="en">
<head>
<meta charset="utf-8">
<title>Bright Path Coaching – Business Card</title>
<link href="https://fonts.googleapis.com/css2?family=Gelasio:wght@400;700&display=swap" rel="stylesheet">
<style>
  :root {
    --page: #eeeae4;
    --card: #ffffff;
    --navy: #0b4a94;
    --sky: #1f92d2;
    --royal-light: #1a62d6;
    --royal-dark: #0a3f8f;
    --rule: #cfcfcf;
    --muted: #a3a3a3;
    --serif: "Gelasio", "Bookman Old Style", Georgia, serif;
  }
  * { box-sizing: border-box; margin: 0; padding: 0; }
  html, body {
    width: 1200px; height: 1000px; overflow: hidden;
    background: var(--page);
    font-family: var(--serif);
  }
  .stage { position: relative; width: 1200px; height: 1000px; }

  .card {
    position: absolute;
    width: 790px; height: 452px;
    box-shadow: 0 3px 10px rgba(0,0,0,.18);
    overflow: hidden;
  }

  /* front */
  .card--front { left: 64px; top: 74px; background: var(--card); }
  .front__band { position: absolute; left: 0; top: 0; width: 26px; height: 100%; background: var(--navy); }
  .front__divider { position: absolute; left: 389px; top: 56px; width: 6px; height: 340px; background: var(--rule); }

  .brand {
    position: absolute; display: flex; flex-direction: column; align-items: center; text-align: center;
  }
  .card--front .brand { left: 100px; top: 150px; width: 210px; color: var(--navy); }
  .brand__mark { width: 30px; height: 30px; border-radius: 50%; margin-bottom: 14px; }
  .card--front .brand__mark { background: var(--navy); }
  .brand__name { font-weight: 700; font-size: 40px; line-height: 1.05; }

  .contact { position: absolute; left: 420px; top: 162px; color: var(--navy); white-space: nowrap; }
  .contact__credentials { font-size: 19px; line-height: 1; font-weight: 400; }
  .contact__name { font-size: 38px; line-height: 1.05; font-weight: 400; }
  .contact__title { font-size: 21px; line-height: 1.1; font-weight: 400; }
  .contact__list { list-style: none; margin-top: 12px; color: var(--muted); font-size: 13.5px; }
  .contact__list li { display: flex; align-items: center; gap: 7px; height: 21px; }
  .contact__icon { width: 13px; height: 13px; flex: none; }
  .contact__icon--dot { border-radius: 50%; background: var(--muted); }
  .contact__icon--at { font-size: 14px; line-height: 13px; text-align: center; }

  /* back */
  .card--back {
    left: 346px; top: 526px;
    background: radial-gradient(ellipse at 45% 30%, var(--royal-light) 0%, #114fbf 45%, var(--royal-dark) 100%);
  }
  .back__strip { position: absolute; right: 0; top: 0; width: 26px; height: 100%; background: var(--card); }
  .card--back .brand { left: 270px; top: 110px; width: 230px; color: #fff; }
  .card--back .brand__mark { background: #fff; }
</style>
</head>
<body>
<main class="stage">

  <section class="card card--front" aria-label="Business card front">
    <div class="front__band"></div>

    <div class="brand">
      <span class="brand__mark"></span>
      <span class="brand__name">Bright Path Coaching</span>
    </div>

    <div class="front__divider"></div>

    <div class="contact">
      <p class="contact__credentials">QTV-AR</p>
      <h1 class="contact__name">Marla Thorncastle</h1>
      <p class="contact__title">Self Empowerment Coach</p>
      <ul class="contact__list">
        <li>
          <svg class="contact__icon" viewBox="0 0 16 16" aria-hidden="true">
            <circle cx="8" cy="8" r="8" fill="#a3a3a3"/>
            <path d="M5.2 3.8l1.6 0 .7 2-1 .9c.5 1.1 1.3 1.9 2.4 2.4l.9-1 2 .7v1.6c0 .5-.5.9-1 .8C7.6 10.9 5.1 8.4 4.4 5.2c-.1-.5.3-1.4.8-1.4z" fill="#fff"/>
          </svg>
          318.557.6021
        </li>
        <li><span class="contact__icon contact__icon--dot"></span>Bright Path Coaching</li>
        <li><span class="contact__icon contact__icon--dot"></span>@BrightPath</li>
        <li><span class="contact__icon contact__icon--at">@</span>mt@thebloomingpathcoach.example</li>
      </ul>
    </div>
  </section>

  <section class="card card--back" aria-label="Business card back">
    <div class="brand">
      <span class="brand__mark"></span>
      <span class="brand__name">Bright Path Coaching</span>
    </div>
    <div class="back__strip"></div>
  </section>

</main>
</body>
</html>
```